Business logo, card, letterhead.

Hospitality Consultancy.

Industry/Entity Type

Business

Contact Information for Business Card

Want dual side card.

Side one with: F
This needs to be soft but standout, probably indented.

Side two has the info below.

Director: Dennis Marlow
0438 215064
PO Box 5816 Kelvin Heights 3188
www.marlowhospitalityconsultancy.com
dennis@marlowhospitalityconsultancy.com

Logo styles of interest
Wordmark Logo

```html
<!DOCTYPE html>
<html lang="en">
<head>
<meta charset="utf-8">
<title>Dennis Marlow – Hospitality Consultant – Business Card</title>
<link rel="stylesheet" href="https://fonts.googleapis.com/css2?family=Josefin+Sans:wght@300;400;600;700&display=swap">
<style>
  :root {
    --backdrop: #d3dee6;
    --card-black: #141414;
    --card-white: #fbfbfa;
    --mark-grey: #8c8c8c;
    --ink-white: #ffffff;
    --ink-dark: #2a2a2a;
    --ink-gold: #a8863a;
    --accent-blue: #2f8fd0;
  }
  html, body {
    margin: 0;
    padding: 0;
    width: 1200px;
    height: 1200px;
    overflow: hidden;
    background: var(--backdrop);
  }
  .canvas {
    position: relative;
    width: 1200px;
    height: 1200px;
    font-family: "Josefin Sans", sans-serif;
  }
  .card {
    position: absolute;
    left: 250px;
    width: 700px;
    height: 400px;
    box-shadow: 0 6px 18px rgba(40, 60, 80, 0.18);
  }

  /* Front side */
  .card-front {
    top: 130px;
    background: var(--card-black);
  }
  .front-mark {
    position: absolute;
    left: 190px;
    top: 95px;
    width: 210px;
    height: 210px;
    background: var(--mark-grey);
  }
  .front-name {
    position: absolute;
    left: 452px;
    top: 200px;
    transform: translate(-50%, -50%) rotate(-90deg);
    white-space: nowrap;
    color: var(--ink-white);
    font-weight: 700;
    font-size: 30px;
    letter-spacing: 2px;
  }

  /* Back side */
  .card-back {
    top: 670px;
    background: var(--card-white);
    color: var(--ink-dark);
  }
  .back-heading {
    position: absolute;
    top: 46px;
    left: 0;
    right: 0;
    text-align: center;
    margin: 0;
    font-weight: 400;
    font-size: 22px;
    letter-spacing: 2px;
    color: var(--ink-gold);
  }
  .back-details {
    position: absolute;
    top: 100px;
    left: 0;
    right: 0;
    text-align: center;
    font-weight: 300;
    font-size: 21px;
    line-height: 30px;
    letter-spacing: 2px;
  }
  .back-details .role {
    color: var(--ink-gold);
  }
  .back-links {
    position: absolute;
    left: 110px;
    top: 268px;
    font-weight: 300;
    font-size: 15px;
    line-height: 24px;
    letter-spacing: 0.5px;
  }
  .back-links p,
  .back-details p {
    margin: 0;
  }
  .social-line {
    display: flex;
    align-items: center;
    gap: 10px;
    margin-left: -24px !important;
  }
  .social-dot {
    width: 14px;
    height: 14px;
    border-radius: 50%;
    background: var(--accent-blue);
  }
</style>
</head>
<body>
<main class="canvas">
  <section class="card card-front" aria-label="Card front">
    <div class="front-mark" aria-hidden="true"></div>
    <p class="front-name">Dennis Marlow</p>
  </section>

  <section class="card card-back" aria-label="Card back">
    <h1 class="back-heading">Hospitality Consultant</h1>
    <div class="back-details">
      <p class="role">Director</p>
      <p>Dennis Marlow</p>
      <p>0438 215064</p>
      <p>PO Box 5816</p>
      <p>Kelvin Heights 3188</p>
    </div>
    <div class="back-links">
      <p>www.marlowhospitalityconsultancy.com</p>
      <p>dennis@marlowhospitalityconsultancy.com</p>
      <p class="social-line"><span class="social-dot" aria-hidden="true"></span>www.social.com/dennismarlow</p>
    </div>
  </section>
</main>
</body>
</html>
```